electrical contractor business card for professional modern company

I need a business card design for an electrical contractors business. I do all kinds of electricical work from new homes, air conditioning, data and communications. I have a logo design i want on it and have a good idea in my head of what i want it to look like. I like simple yet bold and professional looking. All black background is a must

Target Market(s)

Anyone needing electrical work done

Industry/Entity Type

Electrical

Contact Information for Business Card

company name- KTW Electrical and Data
person name-martin pellowe
phone number- 0418 362 927
website-ktwelec.example.com.au

Font styles to use
Sans Serif

Requirements
Must have
• email
• website
• logo
• name
• phone number
• list of work i do:
• -electrical
• -air-conditioning
• -data/communications
• -cctv/security
• -domestic/commercial/industrial
• -24hr emergency breakdown repair
Nice to have
• i would like the logo on the front side in the centre taking up most of the card with black background.
• on the rear i want the list of work i do with company info i.e. email, website, my name, phone number. rear of card also black background with orange writing to match the orange in the logo

```html
<!DOCTYPE html>
<html lang="en">
<head>
<meta charset="utf-8">
<title>KTW Electrical and Data – Business Card</title>
<link rel="stylesheet" href="https://fonts.googleapis.com/css2?family=Noto+Sans:wght@400;600&display=swap">
<style>
  :root {
    --page: #ffffff;
    --card: #000000;
    --band: #3b3b3b;
    --orange: #f36b33;
    --bullet: #ffffff;
    --font: "Noto Sans", sans-serif;
  }
  * { margin: 0; padding: 0; box-sizing: border-box; }
  html, body { width: 1200px; height: 900px; overflow: hidden; background: var(--page); }
  body { position: relative; font-family: var(--font); color: var(--orange); }

  .card { position: absolute; background: var(--card); }

  /* Front face */
  .card-front { left: 0; top: 0; width: 722px; height: 422px; }
  .brand {
    position: absolute; left: 0; right: 0; top: 150px;
    text-align: center; font-weight: 600; color: var(--orange); line-height: 1;
  }
  .brand-name { display: block; font-size: 88px; letter-spacing: 4px; }
  .brand-tag { display: block; font-size: 22px; letter-spacing: 1px; margin-top: 16px; }

  /* Back face */
  .card-back { left: 478px; top: 454px; width: 722px; height: 446px; }
  .band { position: absolute; left: 0; width: 100%; background: var(--band); }
  .band-top { top: 0; height: 52px; }
  .band-bottom { bottom: 0; height: 52px; }
  .company-title {
    position: absolute; left: 48px; top: 4px; font-size: 40px; font-weight: 400; line-height: 44px;
  }
  .contact {
    position: absolute; right: 22px; top: 56px; text-align: right;
    font-size: 28px; line-height: 40px; letter-spacing: 1px;
  }
  .deals-heading {
    position: absolute; left: 18px; top: 150px; font-size: 34px; font-weight: 400; letter-spacing: 1px;
  }
  .services {
    position: absolute; left: 40px; top: 198px; list-style: none;
    font-size: 25px; line-height: 26px; letter-spacing: 0.5px;
  }
  .services li { position: relative; padding-left: 56px; }
  .services li::before {
    content: ""; position: absolute; left: 0; top: 6px;
    width: 26px; height: 14px; border-radius: 50%; background: var(--bullet);
  }
  .email {
    position: absolute; left: 112px; top: 3px; font-size: 31px; line-height: 46px; letter-spacing: 1px;
  }
</style>
</head>
<body>
  <section class="card card-front" aria-label="Card front">
    <p class="brand">
      <span class="brand-name">KTW</span>
      <span class="brand-tag">ELECTRICAL AND DATA</span>
    </p>
  </section>

  <section class="card card-back" aria-label="Card back">
    <div class="band band-top">
      <h1 class="company-title">KTW Electricals and data</h1>
    </div>
    <p class="contact">MARTIN PELLOWE<br>PH:-0418362927</p>
    <h2 class="deals-heading">DEALS IN:-</h2>
    <ul class="services">
      <li>ELECTRICAL FITTING</li>
      <li>AIR- CONDITIONING</li>
      <li>DATA/COMMUNICATIONS</li>
      <li>CCTV/SECURITY</li>
      <li>DOMESTIC/COMERCIAL/INDUSTRIAL</li>
      <li>24 HR EMERGENCY BREAKDOWN REPAIR</li>
    </ul>
    <div class="band band-bottom">
      <p class="email">email:- ktwelec.example.com.au</p>
    </div>
  </section>
</body>
</html>
```